Bref créative
Talbert Commercial Real Estate Stationary
Business Cards, Letterhead, Fax Cover, Envelopes, Thank You Cards/Envelopes, Header & Footer
Professional
Paul Everett Talbert, Jr.
Vice President
20483 Wexmoor Road, Suite 240
Little Rock, Arkansas 72399
PETalbert@talbertcommercial-example.com
www.talbertcommercial-example.com
We would also like a powerpoint presentation if you could include that in your designs.
Thanks for all your help and God bless!
Put the Talbert Commercial logo on the back of the card or just the "R" part of the logo. We also want the following listed for our services:
Brokerage, Construction, Development, Leasing, Management
Talbert Commercial Logo Design

```html
<!DOCTYPE html>
<html lang="en">
<head>
<meta charset="utf-8">
<title>Talbert Commercial Real Estate Stationery</title>
<link href="https://fonts.googleapis.com/css2?family=Roboto:wght@400;700&display=swap" rel="stylesheet">
<style>
  :root {
    --red: #c92a2a;
    --red-dark: #a31e22;
    --ink: #3a3a3a;
    --grey: #8a8a8a;
    --line: #c9c9c9;
    --paper: #ffffff;
    --backdrop: #e9e6e2;
    --faint: #f6e3e3;
  }
  * { box-sizing: border-box; margin: 0; padding: 0; }
  html, body { width: 1200px; height: 560px; overflow: hidden; }
  body {
    background: var(--backdrop);
    font-family: "Roboto", Arial, sans-serif;
    color: var(--ink);
    position: relative;
  }
  .sheet, .card, .envelope {
    position: absolute;
    background: var(--paper);
    box-shadow: 0 2px 6px rgba(0,0,0,.18);
    overflow: hidden;
  }
  .brand { display: flex; align-items: center; gap: 5px; }
  .brand-square { width: 14px; height: 14px; background: var(--red); }
  .brand-name { font-weight: 700; color: var(--red); font-size: 20px; letter-spacing: .5px; line-height: 1; }
  .brand-sub { font-size: 5px; color: var(--grey); letter-spacing: 1.5px; text-transform: uppercase; }

  .contact { font-size: 5px; line-height: 7px; color: var(--grey); position: absolute; }

  .watermark {
    position: absolute; font-weight: 700; color: var(--faint);
    font-size: 60px; letter-spacing: 2px;
  }
  .footer-band {
    position: absolute; left: 0; right: 0; bottom: 0; height: 28px;
    background: linear-gradient(var(--red) 0 6px, var(--paper) 6px 9px, var(--red-dark) 9px);
    color: #fff; font-size: 6px; text-align: center; padding-top: 14px; letter-spacing: .5px;
  }

  /* letterhead */
  .sheet { top: 72px; width: 336px; height: 451px; }
  .sheet.fax { left: 65px; }
  .sheet.letter { left: 427px; }
  .sheet .brand { position: absolute; left: 22px; top: 26px; }
  .sheet .contact { left: 170px; top: 24px; }
  .sheet .watermark { left: 40px; top: 220px; }

  .fax-form {
    position: absolute; left: 22px; top: 78px; width: 292px; height: 100px;
    border: 1px solid var(--line); border-radius: 4px; padding: 10px 12px;
    display: grid; grid-template-columns: 1fr 1fr; column-gap: 14px; row-gap: 9px;
    font-size: 6px; color: var(--grey);
  }
  .fax-field { border-bottom: 1px solid var(--line); padding-bottom: 2px; }
  .fax-checks {
    position: absolute; left: 22px; top: 186px; display: flex; gap: 9px;
    font-size: 5.5px; color: var(--grey);
  }
  .fax-checks span::before {
    content: ""; display: inline-block; width: 5px; height: 5px;
    border: 1px solid var(--grey); margin-right: 3px; vertical-align: -1px;
  }
  .fax-comments { position: absolute; left: 22px; top: 204px; font-size: 6px; color: var(--grey); }

  /* cards */
  .card { width: 187px; height: 108px; }
  .card.front { left: 775px; top: 79px; }
  .card.front .brand { position: absolute; left: 70px; top: 12px; }
  .card.front .brand-name { font-size: 15px; }
  .card-person { position: absolute; left: 12px; top: 56px; font-size: 5.5px; line-height: 7px; color: var(--grey); }
  .card-person strong { color: var(--red); font-size: 6px; }
  .card-strip { position: absolute; left: 0; right: 0; bottom: 0; height: 8px; background: var(--red); }

  .card.back { left: 962px; top: 192px; width: 206px; height: 115px; }
  .back-block {
    position: absolute; left: 0; top: 0; width: 104px; height: 100%;
    background: var(--red); display: flex; align-items: center; justify-content: center;
  }
  .back-block .brand-name { color: #fff; font-size: 15px; }
  .services { position: absolute; left: 118px; top: 26px; list-style: none; font-size: 6px; line-height: 11px; color: var(--ink); }
  .services li::before { content: ""; display: inline-block; width: 3px; height: 3px; background: var(--red); margin-right: 4px; vertical-align: 1px; }

  /* envelopes */
  .envelope { width: 358px; height: 120px; }
  .envelope.rear { left: 808px; top: 317px; }
  .envelope.front { left: 775px; top: 390px; }
  .flap { position: absolute; left: 0; top: 0; width: 100%; height: 52px; }
  .envelope .footer-band { height: 22px; padding-top: 11px; }
  .envelope .brand { position: absolute; left: 14px; top: 14px; }
  .envelope .brand-name { font-size: 14px; }
  .envelope .contact { left: 14px; top: 34px; }
</style>
</head>
<body>

<!-- Fax cover -->
<section class="sheet fax">
  <div class="brand"><div class="brand-square"></div><div><div class="brand-name">TALBERT</div><div class="brand-sub">Commercial</div></div></div>
  <div class="contact">20483 Wexmoor Road, Suite 240<br>Little Rock, Arkansas 72399<br>T 501.555.0142<br>F 501.555.0143<br>PETalbert@talbertcommercial-example.com</div>
  <div class="fax-form">
    <div class="fax-field">To:</div><div class="fax-field">From:</div>
    <div class="fax-field">Fax:</div><div class="fax-field">Pages:</div>
    <div class="fax-field">Phone:</div><div class="fax-field">Date:</div>
    <div class="fax-field">Re:</div><div class="fax-field">CC:</div>
  </div>
  <div class="fax-checks"><span>Urgent</span><span>For Review</span><span>Please Comment</span><span>Please Reply</span><span>Please Recycle</span></div>
  <div class="fax-comments">Comments:</div>
  <div class="watermark">TALBERT</div>
  <div class="footer-band">www.talbertcommercial-example.com</div>
</section>

<!-- Letterhead -->
<section class="sheet letter">
  <div class="brand"><div class="brand-square"></div><div><div class="brand-name">TALBERT</div><div class="brand-sub">Commercial</div></div></div>
  <div class="contact">20483 Wexmoor Road, Suite 240<br>Little Rock, Arkansas 72399<br>T 501.555.0142<br>F 501.555.0143<br>PETalbert@talbertcommercial-example.com</div>
  <div class="watermark">TALBERT</div>
  <div class="footer-band">www.talbertcommercial-example.com</div>
</section>

<!-- Business card front -->
<section class="card front">
  <div class="brand"><div class="brand-square"></div><div><div class="brand-name">TALBERT</div><div class="brand-sub">Commercial</div></div></div>
  <div class="card-person"><strong>Paul Everett Talbert, Jr.</strong><br>Vice President<br>T 501.555.0142<br>PETalbert@talbertcommercial-example.com<br>www.talbertcommercial-example.com</div>
  <div class="card-strip"></div>
</section>

<!-- Business card back -->
<section class="card back">
  <div class="back-block"><div class="brand-name">TALBERT</div></div>
  <ul class="services"><li>Brokerage</li><li>Construction</li><li>Development</li><li>Leasing</li><li>Management</li></ul>
</section>

<!-- Envelopes -->
<section class="envelope rear">
  <svg class="flap" viewBox="0 0 358 52" preserveAspectRatio="none"><path d="M0 0H358V10L179 52L0 10Z" fill="#c92a2a"/></svg>
  <div class="footer-band">www.talbertcommercial-example.com</div>
</section>
<section class="envelope front">
  <div class="brand"><div class="brand-square"></div><div class="brand-name">TALBERT</div></div>
  <div class="contact">20483 Wexmoor Road, Suite 240<br>Little Rock, Arkansas 72399</div>
  <div class="footer-band">www.talbertcommercial-example.com</div>
</section>

</body>
</html>
```